Website needed for Entertainment Company [Wordpress & Mobile Site] (Contest)

"Tumble Scholars" does Acrobatic Educational Shows for schools.
We need a 4-Page Wordpress site, for BOTH Desktop & Mobile
THINGS WE'D LIKE ON THE HOME PAGE
- Book Now buttons
- Panel advertising "Kindness-Shield Tumbling Tour" with subheading "Educating the Victim, Empowering the Bystander, and Enlightening the Bully" with Photo & 'Read More'
- text somewhere saying "Tumble Scholars engages children in important topics, by utilising Parkour & Acrobatics to captivate and enthrall todays youngest generation."
- Panel advertising Teachers Resources: "Curriculum based resources for teachers including lesson plans, workbooks, and physical activities for before & after the show." Maybe even some boxes that say a subject that is covered (eg. Mathematics. Science. PD/H/PE.)
- Everything else that you recommend
4 PAGES:
- Home Page
- About Us
- Our Program & Shows
- Teachers Resources Portal
NOTE: Transparent & Source files for logo will be provided soon (recently finished being designed)

```html
<!DOCTYPE html>
<html lang="en">
<head>
<meta charset="utf-8">
<title>Tumble Scholars – Acrobatic Educational Shows for Schools</title>
<link href="https://fonts.googleapis.com/css2?family=Open+Sans:wght@400;600;700;800&display=swap" rel="stylesheet">
<style>
:root{
  --orange:#f7931e;
  --blue:#29a8e0;
  --navy:#1d3f5e;
  --green:#6cc04a;
  --ink:#333;
  --muted:#777;
  --dark:#3b3b3b;
  --line:#d8d8d8;
  --paper:#fff;
}
*{box-sizing:border-box;margin:0;padding:0}
html,body{width:1200px;height:4052px;overflow:hidden}
body{font-family:"Open Sans",Arial,sans-serif;color:var(--ink);background:var(--paper);position:relative}
section,header,footer{position:absolute;left:0;width:1200px}
.brand{font-weight:800;font-size:34px;color:var(--orange);display:flex;align-items:center;gap:10px;letter-spacing:-.5px}
.brand-dot{width:18px;height:18px;border-radius:50%;background:var(--blue)}

/* header */
.site-header{top:0;height:100px;background:#fff;box-shadow:0 2px 6px rgba(0,0,0,.08);z-index:5}
.site-header .brand{position:absolute;left:40px;top:28px}
.contact-bar{position:absolute;right:40px;top:12px;display:flex;gap:22px;font-size:13px;color:var(--muted);align-items:center}
.contact-bar span{display:flex;align-items:center;gap:6px}
.social-dots{display:flex;gap:6px}
.social-dots i{width:16px;height:16px;border-radius:50%;background:var(--blue);display:block}
.main-nav{position:absolute;right:40px;top:52px;display:flex;gap:30px;align-items:center;font-size:14px;font-weight:600}
.main-nav a{color:var(--ink);text-decoration:none;padding-bottom:6px}
.main-nav a.active{border-bottom:3px solid var(--green)}
.btn{display:inline-block;font-weight:700;color:#fff;text-decoration:none;text-align:center;border-radius:3px}
.btn-book{background:var(--orange);padding:9px 16px;font-size:14px}

/* hero */
.hero{top:100px;height:660px;background:linear-gradient(180deg,#eef0f2,#f7f8f9 70%,#fff)}
.hero-photo{position:absolute;left:60px;top:20px;width:620px;height:610px;background:radial-gradient(ellipse at 50% 45%,#d9b59c 0%,#cfd2d6 45%,rgba(238,240,242,0) 72%)}
.hero-title{position:absolute;left:710px;top:210px;width:440px;font-size:40px;font-weight:700;line-height:1.22;color:#3d3d3d}
.hero-chevron{position:absolute;left:0;top:620px}

/* feature */
.feature{top:760px;height:480px;background:#fff}
.feature-text{position:absolute;left:90px;top:70px;width:560px}
.feature h2{font-size:30px;font-weight:800;letter-spacing:-.5px}
.feature h2 .o{color:var(--orange)} .feature h2 .b{color:var(--blue)}
.feature h3{font-size:20px;font-weight:700;color:#444;margin-top:10px;line-height:1.35}
.feature p{font-size:18px;color:var(--muted);margin-top:18px;line-height:1.5}
.btn-learn{background:var(--navy);padding:12px 38px;font-size:17px;margin-top:26px;box-shadow:0 3px 0 #0f2638}
.feature-photo{position:absolute;left:700px;top:30px;width:460px;height:430px;background:linear-gradient(160deg,#f4f6f8,#cfe8ec 55%,#e9ecef)}

/* programs */
.programs{top:1240px;height:760px;background:linear-gradient(180deg,#2f2f2f,#4a4a4a 60%,#3a3a3a)}
.programs-texture{position:absolute;inset:0;background:linear-gradient(120deg,rgba(255,255,255,.05),rgba(0,0,0,.25))}
.section-title{font-size:30px;font-weight:800;text-align:center;color:var(--orange);letter-spacing:.5px}
.programs .section-title{position:absolute;top:90px;width:100%}
.program-card{position:absolute;top:150px;width:450px;height:470px;background:#fff;box-shadow:0 4px 12px rgba(0,0,0,.4)}
.program-card .photo{height:250px}
.card-acro{left:145px} .card-acro .photo{background:linear-gradient(135deg,#efe7df,#c99a78)}
.card-park{left:605px} .card-park .photo{background:linear-gradient(180deg,#b9c8d4,#e7ecef 60%,#9aa7b0)}
.program-tag{position:absolute;top:215px;right:0;width:200px;height:56px;color:#fff;font-weight:800;font-size:20px;display:flex;align-items:center;justify-content:center;gap:10px;letter-spacing:1px}
.card-acro .program-tag{background:var(--orange)} .card-park .program-tag{background:var(--blue)}
.program-card p{padding:34px 22px 0;font-size:15px;color:var(--muted);line-height:1.55}
.program-card .bar{position:absolute;bottom:0;left:0;right:0;height:8px}
.card-acro .bar{background:var(--orange)} .card-park .bar{background:var(--blue)}
.slider-arrow{position:absolute;top:400px;width:36px;height:36px;border-radius:50%;background:#ddd;display:flex;align-items:center;justify-content:center}
.arrow-prev{left:62px} .arrow-next{right:62px}
.btn-view{position:absolute;left:490px;top:662px;width:220px;background:var(--blue);padding:11px 0;font-size:17px;box-shadow:0 3px 0 #15759f}
.programs-chevron{position:absolute;left:0;top:690px}

/* resources */
.resources{top:2000px;height:560px;background:#fff}
.resources h2{position:absolute;top:170px;left:150px;width:900px;text-align:center;font-size:31px;font-weight:800;line-height:1.35;color:#444}
.resources h2 .o{color:var(--orange)} .resources h2 .b{color:var(--blue)}
.subject{position:absolute;top:315px;width:160px;height:190px;border:2px solid var(--line);background:#fff;display:flex;flex-direction:column;align-items:center;justify-content:flex-end;padding-bottom:18px;font-size:17px;font-weight:600;color:#444}
.subject svg{position:absolute;top:28px;left:40px}
.subject-math{left:300px} .subject-sci{left:520px} .subject-pe{left:740px}

/* engage */
.engage{top:2560px;height:480px;background:linear-gradient(180deg,#5a5a5a,#3d3d3d)}
.engage-photo{position:absolute;left:40px;top:40px;width:560px;height:380px;background:radial-gradient(ellipse at 50% 50%,#c79a80 0%,#7a7a70 40%,rgba(70,70,70,0) 72%)}
.engage p{position:absolute;left:540px;top:170px;width:560px;color:#fff;font-size:29px;font-weight:700;line-height:1.38}
.engage-chevron{position:absolute;left:0;top:400px}

/* booking */
.booking{top:3040px;height:480px;background:#fff}
.booking .section-title{position:absolute;top:70px;width:100%}
.booking-form{position:absolute;left:120px;top:140px;width:960px;height:300px;border:2px solid var(--line);background:#fff}
.form-tabs{display:flex;height:42px;background:var(--blue)}
.form-tabs span{display:flex;align-items:center;padding:0 26px;color:#fff;font-size:14px;font-weight:700}
.form-tabs .label{background:#fff;color:#444;border-right:1px solid var(--line)}
.form-tabs .active{background:var(--orange)}
.field{position:absolute;height:34px;border:1px solid #cfcfcf;font-size:12px;color:#555;padding:9px 10px}
.field-area{height:110px}
.btn-send,.btn-reset{position:absolute;top:232px;width:80px;padding:8px 0;font-size:12px}
.btn-send{left:680px;background:var(--green)} .btn-reset{left:774px;background:var(--orange)}

/* footer */
.site-footer{top:3520px;height:532px;background:#fff;border-top:1px solid #eee}
.site-footer .brand{position:absolute;left:0;width:100%;justify-content:center;top:70px;font-size:40px}
.footer-cols{position:absolute;top:220px;left:70px;width:1060px;display:flex;justify-content:space-between}
.footer-col h4{font-size:14px;font-weight:800;margin-bottom:14px;letter-spacing:.5px}
.footer-col li{list-style:none;font-size:13px;color:var(--muted);line-height:1.7;display:flex;align-items:center;gap:8px}
.footer-col li i{width:14px;height:14px;border-radius:50%;background:var(--blue);display:inline-block}
.news{display:flex}
.news span{border:1px solid #ccc;font-size:12px;color:#999;padding:8px 10px;width:150px}
.news b{background:var(--green);color:#fff;font-size:12px;padding:8px 12px}
.copyright{position:absolute;bottom:0;left:0;width:100%;height:52px;background:#f2f2f2;display:flex;align-items:center;justify-content:center;font-size:12px;color:#999;letter-spacing:.5px}
</style>
</head>
<body>

<header class="site-header">
  <div class="brand"><span class="brand-dot"></span>Tumble Scholars</div>
  <div class="contact-bar">
    <span><svg width="14" height="14" viewBox="0 0 24 24"><path d="M6.6 10.8a15 15 0 0 0 6.6 6.6l2.2-2.2c.3-.3.7-.4 1-.2 1.1.4 2.3.6 3.6.6.6 0 1 .4 1 1V20c0 .6-.4 1-1 1A17 17 0 0 1 3 4c0-.6.4-1 1-1h3.5c.6 0 1 .4 1 1 0 1.3.2 2.5.6 3.6.1.3 0 .7-.2 1z" fill="#29a8e0"/></svg>+61 400 555 012</span>
    <span><svg width="14" height="12" viewBox="0 0 24 18"><rect x="1" y="1" width="22" height="16" rx="2" fill="none" stroke="#29a8e0" stroke-width="2"/><path d="M1 2l11 8 11-8" fill="none" stroke="#29a8e0" stroke-width="2"/></svg>hello@tumblescholars.example</span>
    <span class="social-dots"><i></i><i></i><i></i></span>
  </div>
  <nav class="main-nav">
    <a class="active" href="#">Home</a>
    <a href="#">About Us</a>
    <a href="#">Our Program &amp; Shows</a>
    <a href="#">Teachers Resources Portal</a>
    <a class="btn btn-book" href="#">Book Now</a>
  </nav>
</header>

<section class="hero">
  <div class="hero-photo" role="img" aria-label="Two acrobats performing a balancing lift"></div>
  <h1 class="hero-title">Tumble Scholars offers Acrobatic Educational Shows for schools</h1>
  <svg class="hero-chevron" width="1200" height="40" viewBox="0 0 1200 40">
    <path d="M0 4 L560 4 L585 32 L610 4 L1200 4" fill="none" stroke="#f7931e" stroke-width="5"/>
    <path d="M0 12 L555 12 L585 40 L615 12 L1200 12" fill="none" stroke="#29a8e0" stroke-width="3" opacity=".6"/>
  </svg>
</section>

<section class="feature">
  <div class="feature-text">
    <h2><span class="o">Kindness-Shield</span> <span class="b">Tumbling</span> <span class="o">Tour</span></h2>
    <h3>Educating the Victim, Empowering the Bystander, and Enlightening the Bully</h3>
    <p>Lorem ipsum dolor sit amet, consectetur adipiscing elit, sed do eiusmod tempor incididunt ut labore et dolore magna aliqua.</p>
    <a class="btn btn-learn" href="#">Learn More</a>
  </div>
  <div class="feature-photo" role="img" aria-label="Aerial performer on blue silks"></div>
</section>

<section class="programs">
  <div class="programs-texture" role="img" aria-label="Darkened photo of a performer in mid-leap"></div>
  <h2 class="section-title">PROGRAM &amp; SHOWS</h2>
  <div class="slider-arrow arrow-prev"><svg width="14" height="14" viewBox="0 0 14 14"><path d="M9 2L4 7l5 5" fill="none" stroke="#333" stroke-width="2.5"/></svg></div>
  <article class="program-card card-acro">
    <div class="photo" role="img" aria-label="Acrobat performing a split balance"></div>
    <div class="program-tag">ACROBATIC</div>
    <p>Lorem ipsum dolor sit amet, consectetur adipiscing elit, sed do eiusmod tempor incididunt ut labore et dolore magna aliqua. Ut enim ad minim veniam, quis nostrud exercitation.</p>
    <div class="bar"></div>
  </article>
  <article class="program-card card-park">
    <div class="photo" role="img" aria-label="Parkour athlete jumping between city buildings"></div>
    <div class="program-tag">PARKOUR</div>
    <p>Lorem ipsum dolor sit amet, consectetur adipiscing elit, sed do eiusmod tempor incididunt ut labore et dolore magna aliqua. Ut enim ad minim veniam, quis nostrud exercitation.</p>
    <div class="bar"></div>
  </article>
  <div class="slider-arrow arrow-next"><svg width="14" height="14" viewBox="0 0 14 14"><path d="M5 2l5 5-5 5" fill="none" stroke="#333" stroke-width="2.5"/></svg></div>
  <a class="btn btn-view" href="#">View All</a>
  <svg class="programs-chevron" width="1200" height="70" viewBox="0 0 1200 70">
    <path d="M0 30 L560 30 L600 62 L640 30 L1200 30 L1200 70 L0 70z" fill="#fff"/>
    <path d="M0 30 L560 30 L600 62 L640 30 L1200 30" fill="none" stroke="#6cc04a" stroke-width="6"/>
  </svg>
</section>

<section class="resources">
  <h2><span class="o">Curriculum based resources</span> for teachers including lesson plans, workbooks, and physical activities <span class="b">for before &amp; after the show</span></h2>
  <div class="subject subject-math">
    <svg width="80" height="80" viewBox="0 0 80 80"><g fill="none" stroke="#f7931e" stroke-width="3"><rect x="4" y="4" width="32" height="32" rx="4"/><rect x="44" y="4" width="32" height="32" rx="4"/><rect x="4" y="44" width="32" height="32" rx="4"/><rect x="44" y="44" width="32" height="32" rx="4"/><path d="M20 12v16M12 20h16M52 20h16M14 54l12 12M26 54L14 66M52 57h16M52 63h16"/></g></svg>
    Mathematics
  </div>
  <div class="subject subject-sci">
    <svg width="80" height="80" viewBox="0 0 80 80"><g fill="none" stroke="#6cc04a" stroke-width="3"><path d="M30 6h20M34 6v24L16 66c-2 5 1 8 6 8h36c5 0 8-3 6-8L46 30V6"/><path d="M24 52h32"/></g></svg>
    Science
  </div>
  <div class="subject subject-pe">
    <svg width="80" height="80" viewBox="0 0 80 80"><g fill="none" stroke="#29a8e0" stroke-width="3"><ellipse cx="40" cy="40" rx="34" ry="12"/><ellipse cx="40" cy="40" rx="34" ry="12" transform="rotate(60 40 40)"/><ellipse cx="40" cy="40" rx="34" ry="12" transform="rotate(-60 40 40)"/></g><circle cx="40" cy="40" r="5" fill="#29a8e0"/></svg>
    PD/H/PE
  </div>
</section>

<section class="engage">
  <div class="engage-photo" role="img" aria-label="Two performers in a dynamic acrobatic pose"></div>
  <p>Tumble Scholars engages children in important topics, by utilising Parkour &amp; Acrobatics to captivate and enthrall todays youngest generation.</p>
  <svg class="engage-chevron" width="1200" height="80" viewBox="0 0 1200 80">
    <path d="M0 40 L520 40 L560 72 L600 40 L1200 40 L1200 80 L0 80z" fill="#fff"/>
    <path d="M0 40 L520 40 L560 72 L600 40 L1200 40" fill="none" stroke="#29a8e0" stroke-width="6"/>
  </svg>
</section>

<section class="booking">
  <h2 class="section-title">BOOK NOW</h2>
  <form class="booking-form">
    <div class="form-tabs">
      <span class="label">PROGRAM</span>
      <span class="active">01. Acrobatic</span>
      <span>02. Parkour</span>
      <span>03. Other</span>
    </div>
    <div class="field" style="left:24px;top:70px;width:300px">First Name</div>
    <div class="field" style="left:344px;top:70px;width:300px">Email</div>
    <div class="field field-area" style="left:664px;top:70px;width:270px">Delivery Address</div>
    <div class="field" style="left:24px;top:120px;width:300px">Last Name</div>
    <div class="field" style="left:344px;top:120px;width:300px">Desired Date</div>
    <div class="field" style="left:24px;top:170px;width:300px">Phone Number</div>
    <div class="field" style="left:344px;top:170px;width:300px">Desired Time</div>
    <a class="btn btn-send" href="#">SEND</a>
    <a class="btn btn-reset" href="#">RESET</a>
  </form>
</section>

<footer class="site-footer">
  <div class="brand"><span class="brand-dot"></span>Tumble Scholars</div>
  <div class="footer-cols">
    <div class="footer-col"><h4>QUICK LINKS</h4><ul><li>Home</li><li>About Us</li><li>Our Program &amp; Shows</li><li>Teachers Resources Portal</li><li>Book Now</li></ul></div>
    <div class="footer-col"><h4>PROGRAM &amp; SHOWS</h4><ul><li>Acrobatic</li><li>Parkour</li></ul></div>
    <div class="footer-col"><h4>CONTACT</h4><ul><li>Tumble Scholars Pty Ltd</li><li>42 Cartwheel Lane</li><li>Fitzroy, VIC</li><li>+61 400 555 012</li><li>hello@tumblescholars.example</li></ul></div>
    <div class="footer-col"><h4>FOLLOW US</h4><ul><li><i></i>Community</li><li><i></i>Updates</li><li><i></i>Gallery</li></ul></div>
    <div class="footer-col"><h4>NEWSLETTER</h4><div class="news"><span>Enter Email Address</span><b>SIGN UP</b></div></div>
  </div>
  <div class="copyright">COPYRIGHT © 2016 TUMBLE SCHOLARS. ALL RIGHTS RESERVED</div>
</footer>

</body>
</html>
```